Business Card Design for an Investment Company

We need a business card design for our private investment company, called Ashbourne Partners. Ashbourne Partners is an investments partnership that aims to acquire shares in listed companies with a view to influencing those companies through active dialogue in order to improve their value. We need designs that use the logo colors (blue, grey, white), we need both English and Arabic on the business cards (can be on one side or 2 sides). The final logo should communicate professionalism, conservatism (nothing too fancy or too cheesy), that we are smart, conservative and old school.

Target Market(s)

Investment companies

Industry/Entity Type

Investment

Contact Information for Business Card

Khalid Yousef Rumaithi
Senior Executive Officer

Palm Terrace 07, Level 3, Office 215/12
HLMZ

+9714987650
krumaithi@ashbournepartners.com
www.ashbournepartners.com

Requirements
Must have
• Logo to be placed on the left hand side of the business card
• for the Arabic, we only need to have the name and title so it can be accomodated on one side so we can have the other side with full color and logo. The arabic that needs to be used is the below:
• خالد يوسف الرميثي
• المدير التنفيدي

```html
<!DOCTYPE html>
<html lang="en">
<head>
<meta charset="utf-8">
<title>Ashbourne Partners — Business Card</title>
<link href="https://fonts.googleapis.com/css2?family=Roboto:wght@400;500&family=Roboto+Slab:wght@300;400&family=Noto+Naskh+Arabic:wght@400;500&display=swap" rel="stylesheet">
<style>
  :root {
    --brand-blue: #0a6aa1;
    --brand-grey: #58595b;
    --paper: #ffffff;
    --ink: #4a4b4d;
    --soft-ink: #dcdcdc;
    --backdrop: #e4e7e8;
  }
  * { margin: 0; padding: 0; box-sizing: border-box; }
  html, body { width: 1200px; height: 960px; overflow: hidden; background: var(--backdrop); }
  .sheet { position: relative; width: 1200px; height: 960px; }

  .card {
    position: absolute; top: 90px; width: 460px; height: 780px;
    box-shadow: 0 6px 18px rgba(0,0,0,0.12);
    overflow: hidden;
  }
  .card--back { left: 110px; background: var(--brand-grey); }
  .card--front { left: 630px; background: var(--paper); }

  .wordmark {
    position: absolute; left: 0; right: 0; text-align: center;
    font-family: "Roboto", sans-serif; font-weight: 500; font-size: 38px; letter-spacing: -0.5px;
  }
  .card--back .wordmark { top: 300px; color: var(--paper); }
  .card--front .wordmark { top: 64px; color: var(--brand-blue); }

  .back-rule {
    position: absolute; top: 372px; left: 50%; width: 120px; height: 3px;
    margin-left: -60px; background: var(--paper);
  }

  .identity-band {
    position: absolute; top: 180px; left: 0; right: 0; height: 270px;
    background: var(--brand-grey);
    border-top: 5px solid var(--brand-blue);
    border-bottom: 5px solid var(--brand-blue);
    color: #f2f2f2;
  }
  .identity__name {
    position: absolute; top: 42px; left: 24px; right: 24px; text-align: center;
    font-family: "Roboto Slab", serif; font-weight: 400; font-size: 26px; line-height: 1.2;
  }
  .identity__title {
    position: absolute; top: 88px; left: 24px; right: 24px; text-align: center;
    font-family: "Roboto Slab", serif; font-weight: 300; font-size: 16px; color: var(--soft-ink);
  }
  .identity__name-ar, .identity__title-ar {
    position: absolute; left: 24px; right: 24px; text-align: center;
    font-family: "Noto Naskh Arabic", serif; direction: rtl; line-height: 1.3;
  }
  .identity__name-ar { top: 124px; font-size: 28px; }
  .identity__title-ar { top: 176px; font-size: 26px; }

  .contacts {
    position: absolute; top: 520px; left: 54px; right: 20px; list-style: none;
    font-family: "Roboto Slab", serif; font-size: 18px; color: var(--ink);
  }
  .contacts__item { display: flex; align-items: flex-start; gap: 14px; margin-bottom: 24px; line-height: 1.35; }
  .contacts__icon { width: 18px; height: 18px; flex: none; margin-top: 3px; fill: var(--brand-blue); }
</style>
</head>
<body>
<main class="sheet">

  <section class="card card--back" aria-label="Card back">
    <div class="wordmark">Ashbourne Partners</div>
    <div class="back-rule"></div>
  </section>

  <section class="card card--front" aria-label="Card front">
    <div class="wordmark">Ashbourne Partners</div>

    <div class="identity-band">
      <p class="identity__name">Khalid Yousef Rumaithi</p>
      <p class="identity__title">Senior Executive Officer</p>
      <p class="identity__name-ar" lang="ar">خالد يوسف الرميثي</p>
      <p class="identity__title-ar" lang="ar">المدير التنفيدي</p>
    </div>

    <ul class="contacts">
      <li class="contacts__item">
        <svg class="contacts__icon" viewBox="0 0 24 24" aria-hidden="true"><path d="M12 1a8 8 0 0 0-8 8c0 6 8 14 8 14s8-8 8-14a8 8 0 0 0-8-8zm0 11a3 3 0 1 1 0-6 3 3 0 0 1 0 6z"/></svg>
        <span>Palm Terrace 07, Level 3,<br>Office 215/12, HLMZ</span>
      </li>
      <li class="contacts__item">
        <svg class="contacts__icon" viewBox="0 0 24 24" aria-hidden="true"><path d="M6.6 10.8a15 15 0 0 0 6.6 6.6l2.2-2.2c.3-.3.7-.4 1-.2 1.1.4 2.3.6 3.6.6.6 0 1 .4 1 1V20c0 .6-.4 1-1 1A17 17 0 0 1 3 4c0-.6.4-1 1-1h3.5c.6 0 1 .4 1 1 0 1.3.2 2.5.6 3.6.1.3 0 .7-.2 1z"/></svg>
        <span>+9714987650</span>
      </li>
      <li class="contacts__item">
        <svg class="contacts__icon" viewBox="0 0 24 24" aria-hidden="true"><path d="M2 5h20v14H2z M2 5l10 8 10-8" fill="var(--brand-blue)" stroke="#fff" stroke-width="1.5"/></svg>
        <span>krumaithi@ashbournepartners.com</span>
      </li>
      <li class="contacts__item">
        <svg class="contacts__icon" viewBox="0 0 24 24" aria-hidden="true"><circle cx="12" cy="12" r="10"/><path d="M2 12h20M12 2c3 3 3 17 0 20M12 2c-3 3-3 17 0 20" fill="none" stroke="#fff" stroke-width="1.5"/></svg>
        <span>www.ashbournepartners.com</span>
      </li>
    </ul>
  </section>

</main>
</body>
</html>
```